U.S. based testing, inspection, and certification (TIC) company needs a new social media design.

We need a social media design primarily for LinkedIn 1200x1200px for our U.S. based company with international capabilities for performing dozens if not hundreds of testing, inspection, and certification (TIC) services. Our primary services include calibration, chemical analysis, consulting engineering, environmental simulation, forensic engineering, materials testing, mechanical testing, and nondestructive testing. Industries we serve are aerospace/aviation, automotive, chemical, commercial properties, construction, consumer products, defense, energy storage, healthcare, insurance/legal, life science, manufacturing, oil & gas, power generation, pulp & paper, and telecommunications. https://corvintest.example/

Guideline hex colors (primary, secondary): #29aae2, #0b1f3b

The final design should communicate:
1. Trust, Integrity, and Independence
2. Technical Expertise and Accuracy
3. Efficiency and Speed
4. Value-Added Partnership

We previously used a hexagon design that we would like to part ways from; hexagon examples and QVR logos uploaded.

```html
<!DOCTYPE html>
<html lang="en">
<head>
<meta charset="utf-8">
<title>QVR — From confidence to certainty</title>
<link rel="stylesheet" href="https://fonts.googleapis.com/css2?family=Arimo:wght@400;700&family=Roboto+Condensed:wght@700&display=swap">
<style>
  :root {
    --brand-blue: #29aae2;
    --band-blue: #2ba8f5;
    --navy: #0b1f3b;
    --deep-navy: #0a1530;
    --space-dark: #050c1e;
    --space-mid: #103a78;
    --horizon: #3f7fc4;
    --white: #ffffff;
  }
  html, body {
    margin: 0;
    padding: 0;
    overflow: hidden;
    background: var(--white);
  }
  .post {
    position: relative;
    width: 1200px;
    height: 1200px;
    overflow: hidden;
    font-family: "Arimo", Arial, sans-serif;
    color: var(--white);
    background: var(--deep-navy);
  }
  .hero-photo {
    position: absolute;
    left: 0; top: 0;
    width: 1200px; height: 840px;
    background:
      radial-gradient(ellipse 900px 420px at 820px 620px, rgba(140,180,225,0.55), transparent 70%),
      radial-gradient(ellipse 500px 260px at 780px 260px, rgba(120,140,170,0.35), transparent 70%),
      linear-gradient(180deg, var(--space-dark) 0%, var(--space-mid) 45%, var(--horizon) 75%, var(--deep-navy) 100%);
  }
  .brand {
    position: absolute;
    left: 80px; top: 66px;
  }
  .brand-mark {
    display: block;
    font-weight: 700;
    font-size: 150px;
    line-height: 126px;
    letter-spacing: 6px;
  }
  .brand-name {
    display: block;
    margin-top: 8px;
    font-weight: 400;
    font-size: 33px;
    line-height: 40px;
  }
  .headline {
    position: absolute;
    left: 78px; top: 282px;
    margin: 0;
    font-weight: 700;
    font-size: 98px;
    line-height: 118px;
    letter-spacing: -0.5px;
  }
  .photo-circles {
    position: absolute;
    left: 0; top: 0;
  }
  .info-band {
    position: absolute;
    left: 0; top: 862px;
    width: 1200px; height: 338px;
    background: var(--band-blue);
  }
  .tab-shapes {
    position: absolute;
    left: 0; top: 836px;
  }
  .tab-label {
    position: absolute;
    margin: 0;
    font-weight: 700;
    font-size: 25px;
    line-height: 30px;
  }
  .tab-label.services { left: 78px; top: 848px; }
  .tab-label.industries { left: 663px; top: 852px; }
  .list-text {
    position: absolute;
    margin: 0;
    font-family: "Roboto Condensed", "Arial Narrow", sans-serif;
    font-weight: 700;
    font-size: 27px;
    line-height: 35px;
  }
  .list-text.services { left: 79px; top: 906px; width: 520px; }
  .list-text.industries { left: 663px; top: 902px; width: 530px; }
  .divider {
    position: absolute;
    left: 625px; top: 910px;
    height: 262px;
    border-left: 2px dotted var(--navy);
  }
  .site-url {
    position: absolute;
    left: 79px; top: 1136px;
    margin: 0;
    font-weight: 400;
    font-size: 29px;
    line-height: 36px;
    color: var(--navy);
  }
</style>
</head>
<body>
<main class="post">
  <div class="hero-photo" role="img" aria-label="Photograph of a satellite with solar panels orbiting above cloud-covered Earth"></div>

  <div class="brand">
    <span class="brand-mark">QVR</span>
    <span class="brand-name">Quorvin Verification Resources</span>
  </div>

  <h1 class="headline">We take you from<br>confidence to<br>certainty</h1>

  <svg class="photo-circles" width="1200" height="840" viewBox="0 0 1200 840">
    <defs>
      <linearGradient id="valves-fill" x1="0" y1="0" x2="0" y2="1">
        <stop offset="0" stop-color="#6fb6f0"/>
        <stop offset="1" stop-color="#2f7fc0"/>
      </linearGradient>
      <linearGradient id="gauges-fill" x1="0" y1="0" x2="1" y2="1">
        <stop offset="0" stop-color="#d9d6c8"/>
        <stop offset="1" stop-color="#b9a64a"/>
      </linearGradient>
      <linearGradient id="flange-fill" x1="0" y1="0" x2="1" y2="1">
        <stop offset="0" stop-color="#a06a3e"/>
        <stop offset="1" stop-color="#4a3326"/>
      </linearGradient>
    </defs>
    <g role="img" aria-label="Photograph of blue pipeline valves with yellow gas lines under a clear sky">
      <circle cx="1055" cy="390" r="92" fill="url(#valves-fill)" stroke="var(--brand-blue)" stroke-width="4"/>
    </g>
    <g role="img" aria-label="Photograph of pressure gauges on yellow gas pipework">
      <circle cx="945" cy="643" r="147" fill="url(#gauges-fill)" stroke="var(--brand-blue)" stroke-width="4"/>
    </g>
    <g role="img" aria-label="Photograph of a corroded rusty pipe flange">
      <circle cx="625" cy="700" r="110" fill="url(#flange-fill)" stroke="var(--brand-blue)" stroke-width="4"/>
    </g>
  </svg>

  <div class="info-band"></div>

  <svg class="tab-shapes" width="1200" height="54" viewBox="0 0 1200 54">
    <polygon points="0,2 443,2 408,52 0,52" fill="var(--navy)" stroke="var(--brand-blue)" stroke-width="1"/>
    <polygon points="623,4 1066,4 1031,52 623,52" fill="var(--navy)" stroke="var(--brand-blue)" stroke-width="1"/>
  </svg>

  <h2 class="tab-label services">Our primary services</h2>
  <h2 class="tab-label industries">Industries we serve</h2>

  <p class="list-text services">calibration, chemical analysis,<br>consulting engineering,<br>environmental simulation,<br>forensic engineering, materials testing,<br>mechanical testing, and<br>nondestructive testing.</p>

  <div class="divider"></div>

  <p class="list-text industries">aerospace/aviation, automotive, chemical,<br>commercial properties, construction,<br>consumer products, defense,<br>energy storage, healthcare, insurance/legal,<br>life science, manufacturing, oil &amp; gas,<br>power generation, pulp &amp; paper, and<br>telecommunications.</p>

  <p class="site-url">https://corvintest.example/</p>
</main>
</body>
</html>
```